UX Design of Word Status Report

I want a single page UX designed Status Report in Word or Excel as an easy to read project management update document. The key requirements are on the attached pdf. It would be good if the status buttons were dynamic.

Target Market(s)

Project Managers

Industry/Entity Type

Management

Requirements
Must have
• Have added Excel as an additional option to Word if this makes the development easier.

```html
<!DOCTYPE html>
<html lang="en">
<head>
<meta charset="utf-8">
<title>Project Status Report</title>
<link href="https://fonts.googleapis.com/css2?family=Carlito:wght@400;700&family=Roboto:wght@400;700&display=swap" rel="stylesheet">
<style>
:root{
  --navy:#1f4e79;
  --ink:#111;
  --line:#222;
  --green:#00b050;
  --green-dot:#00b000;
  --yellow:#ffff00;
  --red:#e00000;
  --tile-blue:#5b9bd5;
  --tile-orange:#ff6600;
  --toggle:#3a3a3a;
  --muted:#8a8a8a;
  --chart-blue:#8db4e2;
  --chart-orange:#ed7d31;
  --grid:#d9d9d9;
}
*{box-sizing:border-box;margin:0;padding:0}
html,body{width:1200px;height:1200px;overflow:hidden;background:#fff}
body{position:relative;font-family:"Carlito",Calibri,sans-serif;color:var(--ink);font-size:14px}
.sheet{position:absolute;left:0;top:0;width:1240px;height:1200px;transform-origin:20px 60px;transform:scale(0.965)}
.box{position:absolute;border:1.5px solid var(--line);background:#fff}
.abs{position:absolute}
.bar{position:absolute;background:var(--navy);color:#fff;font-weight:700;font-size:16px;display:flex;align-items:center;padding-left:10px}
.cell{position:absolute;display:flex;align-items:center;justify-content:center;border-right:1px solid var(--line);border-bottom:1px solid var(--line);font-size:14px}
ul.notes{list-style:none;position:absolute;font-size:14px;line-height:18px}
ul.notes li{position:relative;padding-left:17px}
ul.notes li::before{content:"";position:absolute;left:2px;top:7px;width:4px;height:4px;background:#000}
.dot{position:absolute;border-radius:50%}
.brand{font-size:30px;color:var(--navy);font-weight:400;display:flex;align-items:center;gap:10px}
.brand .mark{width:22px;height:22px;border-radius:50%;background:#c00000}
.tile{position:absolute;color:#fff;font-family:"Roboto",sans-serif;padding:8px 16px}
.tile small{display:block;font-size:7px;letter-spacing:.5px;text-transform:uppercase}
.tile strong{display:block;font-size:20px;margin-top:8px}
.toggle{position:absolute;width:96px;height:32px;background:var(--toggle);border-radius:3px}
.toggle::after{content:"";position:absolute;right:6px;top:2px;width:28px;height:28px;border-radius:50%;background:var(--yellow)}
.link{text-decoration:underline}
.legend-text{position:absolute;font-size:10px;line-height:13px}
.row-label{position:absolute;left:27px;color:#fff;font-weight:700;font-size:15px}
.row-text{position:absolute;left:238px}
.hline{position:absolute;left:118px;width:597px;height:1px;background:var(--line)}
</style>
</head>
<body>
<div class="sheet">

<!-- Header -->
<div class="box" style="left:20px;top:120px;width:346px;height:72px">
  <div class="brand abs" style="left:8px;top:18px"><span class="mark"></span>Northbeam Consulting</div>
</div>
<div class="bar" style="left:365px;top:120px;width:214px;height:36px">Project Status Report</div>
<div class="bar" style="left:365px;top:156px;width:73px;height:36px">Date</div>
<div class="box" style="left:438px;top:156px;width:141px;height:36px;display:flex;align-items:center;justify-content:center;font-weight:700;font-size:16px">8/6/2016</div>

<div class="bar" style="left:598px;top:120px;width:117px;height:36px">Client</div>
<div class="bar" style="left:598px;top:156px;width:117px;height:36px">Project</div>
<div class="box" style="left:715px;top:120px;width:265px;height:36px;font-weight:700;font-size:15px;padding:8px 14px">Insert Client Name</div>
<div class="box" style="left:715px;top:155px;width:265px;height:37px;font-weight:700;font-size:15px;padding:8px 14px">LedgerPro 2015 Implementation</div>
<div class="box" style="left:979px;top:120px;width:239px;height:72px;display:flex;flex-direction:column;align-items:center;justify-content:center;font-size:14px;line-height:20px">
  <span>Client Logo</span><span>(Insert-&gt;Picture)</span>
</div>

<!-- Project overview -->
<div class="box" style="left:20px;top:231px;width:346px;height:128px"></div>
<div class="abs" style="left:23px;top:234px;width:51px;height:122px;background:#000;border-radius:2px">
  <span class="dot" style="left:12px;top:8px;width:26px;height:26px;background:var(--red)"></span>
  <span class="dot" style="left:12px;top:44px;width:26px;height:26px;background:var(--yellow)"></span>
  <span class="dot" style="left:12px;top:80px;width:26px;height:26px;background:var(--green-dot)"></span>
</div>
<div class="bar" style="left:75px;top:231px;width:160px;height:30px;padding-left:3px">Project Overview</div>
<div class="bar" style="left:235px;top:231px;width:67px;height:30px;justify-content:center;padding:0">%</div>
<div class="bar" style="left:302px;top:231px;width:64px;height:30px;justify-content:center;padding:0">Status</div>
<div class="cell" style="left:75px;top:261px;width:160px;height:26px;border-left:1px solid var(--line)">Budget Spent</div>
<div class="cell" style="left:235px;top:261px;width:67px;height:26px">7%</div>
<div class="cell" style="left:302px;top:261px;width:64px;height:26px;background:var(--green)"></div>
<div class="cell" style="left:75px;top:287px;width:160px;height:26px;border-left:1px solid var(--line)">Scope Delivered</div>
<div class="cell" style="left:235px;top:287px;width:67px;height:26px">6%</div>
<div class="cell" style="left:302px;top:287px;width:64px;height:26px;background:var(--green)"></div>
<div class="cell" style="left:75px;top:313px;width:160px;height:27px;border-left:1px solid var(--line)">Go-Live Date</div>
<div class="cell" style="left:235px;top:313px;width:67px;height:27px;font-size:13px">1/10/2016</div>
<div class="cell" style="left:302px;top:313px;width:64px;height:27px;background:var(--green)"></div>
<div class="cell" style="left:75px;top:340px;width:160px;height:19px;border-left:1px solid var(--line)"></div>
<div class="cell" style="left:235px;top:340px;width:67px;height:19px"></div>

<!-- Current project review -->
<div class="box" style="left:20px;top:379px;width:346px;height:300px"></div>
<div class="bar" style="left:20px;top:379px;width:346px;height:34px">Current Project Review</div>
<ul class="notes" style="left:30px;top:423px;width:320px">
  <li>LedgerPro 2015 Configuration in progress.</li>
  <li>Data cleansing in progress c/o Kestrel IT</li>
</ul>
<div class="abs" style="left:20px;top:581px;width:346px;height:1.5px;background:var(--line)"></div>
<div class="abs" style="left:131px;top:581px;width:1.5px;height:98px;background:var(--line)"></div>
<div class="abs" style="left:253px;top:581px;width:1.5px;height:98px;background:var(--line)"></div>
<div class="abs" style="left:23px;top:584px;width:108px;height:32px;background:var(--toggle)"><span class="dot" style="left:62px;top:3px;width:26px;height:26px;background:var(--yellow)"></span></div>
<div class="abs" style="left:135px;top:584px;width:95px;height:32px;background:var(--toggle)"><span class="dot" style="left:30px;top:3px;width:26px;height:26px;background:var(--green-dot)"></span></div>
<div class="abs" style="left:256px;top:584px;width:102px;height:32px;background:var(--toggle)"><span class="dot" style="left:4px;top:3px;width:26px;height:26px;background:var(--red)"></span></div>
<div class="legend-text" style="left:28px;top:626px;width:100px">Performing to plan or on target..</div>
<div class="legend-text" style="left:145px;top:618px;width:104px">One or more aspect of project viability — time, cost, scope - is at risk.</div>
<div class="legend-text" style="left:271px;top:621px;width:92px">Requires corrective action to meet business objectives.</div>

<!-- Status report -->
<div class="box" style="left:436px;top:231px;width:372px;height:447px"></div>
<div class="bar" style="left:436px;top:231px;width:372px;height:30px">Project Status Report</div>
<ul class="notes" style="left:446px;top:269px;width:350px">
  <li>Install completed May 25th but need to action at later date report database adapter install and configuration after the companies are setup.</li>
  <li>Performed a workstation install with Jordan</li>
  <li>Kestrel IT responsible for backup jobs for DB Server</li>
  <li>Kestrel IT indicated current clustered DB server (2012) will be upgraded over the next few weeks to DB 2014 (won't affect current install if everything migrates successfully)</li>
  <li>Migration templates uploaded in project site</li>
</ul>
<div class="bar" style="left:436px;top:503px;width:372px;height:26px">Decisions Made</div>
<ul class="notes" style="left:449px;top:538px;width:200px">
  <li>Decision - 1</li>
  <li>Decision - 2</li>
</ul>

<!-- Activities / change request / cost -->
<div class="box" style="left:828px;top:231px;width:390px;height:448px"></div>
<div class="bar" style="left:828px;top:231px;width:390px;height:30px">Activities Next Period</div>
<ul class="notes" style="left:838px;top:268px;width:360px"><li>Kestrel IT continue data cleansing</li></ul>
<div class="bar" style="left:828px;top:379px;width:390px;height:34px;padding-left:4px;font-size:15px"><span class="link">Change Request</span>&nbsp;(Last submitted CR# is – n/a )</div>
<div class="abs" style="left:865px;top:421px;font-family:Roboto,sans-serif;font-weight:700;font-size:20px;color:#444">COST OVERVIEW</div>
<div class="abs" style="left:864px;top:463px;font-family:Roboto,sans-serif;font-size:9px;color:#bbb">FRI 5/20/2016 - FRI 10/21/2016</div>
<div class="tile" style="left:862px;top:484px;width:254px;height:62px;background:var(--tile-blue)"><small>Cost</small><strong>$,123,770.03</strong></div>
<div class="tile" style="left:862px;top:552px;width:254px;height:55px;background:var(--tile-blue)"><small>Remaining cost</small><strong style="margin-top:6px">$,114,211.73</strong></div>
<div class="tile" style="left:862px;top:613px;width:145px;height:55px;background:var(--tile-orange)"><small>% Complete</small><strong style="margin-top:6px">7%</strong></div>

<!-- Bottom status table -->
<div class="box" style="left:20px;top:697px;width:1198px;height:382px"></div>
<div class="abs" style="left:20px;top:697px;width:97px;height:382px;background:var(--navy)"></div>
<div class="abs" style="left:117px;top:697px;width:1.5px;height:382px;background:var(--line)"></div>
<div class="abs" style="left:235px;top:697px;width:1.5px;height:382px;background:var(--line)"></div>
<div class="abs" style="left:715px;top:697px;width:1.5px;height:382px;background:var(--line)"></div>

<div class="hline" style="top:756px"></div>
<div class="hline" style="top:810px"></div>
<div class="hline" style="top:863px"></div>
<div class="hline" style="top:920px"></div>
<div class="hline" style="top:973px"></div>
<div class="hline" style="top:1027px"></div>

<div class="row-label" style="top:718px"><span class="link">Schedule</span></div>
<div class="row-label" style="top:774px">Quality</div>
<div class="row-label" style="top:828px"><span class="link">Scope</span></div>
<div class="row-label" style="top:883px"><span class="link">Budget</span></div>
<div class="row-label" style="top:937px"><span class="link">Risks</span></div>
<div class="row-label" style="top:991px"><span class="link">Schedule</span></div>
<div class="row-label" style="top:1044px"><span class="link">Issues</span></div>

<div class="toggle" style="left:126px;top:702px"></div>
<div class="toggle" style="left:126px;top:768px"></div>
<div class="toggle" style="left:126px;top:815px"></div>
<div class="toggle" style="left:126px;top:868px"></div>
<div class="toggle" style="left:126px;top:926px"></div>
<div class="toggle" style="left:126px;top:978px"></div>
<div class="toggle" style="left:126px;top:1032px"></div>

<div class="row-text" style="top:718px">Project currently on track.</div>
<div class="row-text" style="top:775px">No project concern affecting quality identified.</div>
<div class="row-text" style="top:828px">No change in project scope raised.</div>
<div class="row-text" style="top:883px">Within project budget.</div>
<div class="row-text" style="top:938px">No project risks identified.</div>
<div class="row-text" style="top:991px">No project issues reported.</div>
<div class="row-text" style="top:1044px">No action items logged.</div>

<!-- Chart -->
<div class="abs" style="left:757px;top:705px;font-family:Roboto,sans-serif;font-weight:700;font-size:12px;color:#2e75b6">PROGRESS VERSUS COST</div>
<div class="abs" style="left:757px;top:722px;width:430px;font-size:11px;line-height:16px;color:var(--muted)">Progress made versus the cost spent over time. If % Complete line below the cumulative cost line, your project may be over budget.</div>

<svg class="abs" style="left:734px;top:766px" width="459" height="286" viewBox="896 964 459 286" role="img" aria-label="Line chart of cumulative percent complete and cumulative cost by date" font-family="Carlito, sans-serif">
  <rect x="896.5" y="964.5" width="458" height="285" fill="#fff" stroke="#bfbfbf"/>
  <g stroke="var(--grid)" stroke-width="1">
    <line x1="952" y1="978" x2="1240" y2="978"/><line x1="952" y1="998" x2="1240" y2="998"/>
    <line x1="952" y1="1018" x2="1240" y2="1018"/><line x1="952" y1="1038" x2="1240" y2="1038"/>
    <line x1="952" y1="1058" x2="1240" y2="1058"/><line x1="952" y1="1078" x2="1240" y2="1078"/>
    <line x1="952" y1="1098" x2="1240" y2="1098"/><line x1="952" y1="1118" x2="1240" y2="1118"/>
  </g>
  <line x1="952" y1="1138" x2="1240" y2="1138" stroke="#999"/>
  <g font-size="11" fill="#000" text-anchor="end">
    <text x="939" y="982">8</text><text x="939" y="1002">7</text><text x="939" y="1022">6</text>
    <text x="939" y="1042">5</text><text x="939" y="1062">4</text><text x="939" y="1082">3</text>
    <text x="939" y="1102">2</text><text x="939" y="1122">1</text><text x="939" y="1142">0</text>
  </g>
  <g font-size="11" fill="#000">
    <text x="1249" y="982">$160,000.00</text><text x="1249" y="1002">$140,000.00</text>
    <text x="1249" y="1022">$120,000.00</text><text x="1249" y="1042">$100,000.00</text>
    <text x="1249" y="1062">$80,000.00</text><text x="1249" y="1082">$60,000.00</text>
    <text x="1249" y="1102">$40,000.00</text><text x="1249" y="1122">$20,000.00</text>
    <text x="1249" y="1142">$0.00</text>
  </g>
  <text transform="translate(925 1058) rotate(-90)" font-size="11" text-anchor="middle">% COMPLETE</text>
  <text transform="translate(1335 1058) rotate(-90)" font-size="11" text-anchor="middle">CUMULATIVE  COST</text>
  <g font-size="11" text-anchor="end">
    <text transform="translate(979 1146) rotate(-90)">4/25/2016</text>
    <text transform="translate(1000 1146) rotate(-90)">5/9/2016</text>
    <text transform="translate(1022 1146) rotate(-90)">5/23/2016</text>
    <text transform="translate(1044 1146) rotate(-90)">6/6/2016</text>
    <text transform="translate(1066 1146) rotate(-90)">6/20/2016</text>
    <text transform="translate(1088 1146) rotate(-90)">7/4/2016</text>
    <text transform="translate(1109 1146) rotate(-90)">7/18/2016</text>
    <text transform="translate(1131 1146) rotate(-90)">8/1/2016</text>
    <text transform="translate(1153 1146) rotate(-90)">8/15/2016</text>
    <text transform="translate(1175 1146) rotate(-90)">8/29/2016</text>
    <text transform="translate(1197 1146) rotate(-90)">9/12/2016</text>
    <text transform="translate(1219 1146) rotate(-90)">9/26/2016</text>
    <text transform="translate(1241 1146) rotate(-90)">10/10/2016</text>
  </g>
  <polyline fill="none" stroke="var(--chart-blue)" stroke-width="2.5" points="952,1138 997,1138 1018,1058 1040,998 1238,998"/>
  <polyline fill="none" stroke="var(--chart-orange)" stroke-width="2.5" points="952,1138 1018,1138 1040,1100 1062,1077 1084,1058 1105,1017 1127,1015 1149,1008 1171,1005 1193,1002 1215,998 1238,998"/>
  <line x1="941" y1="1230" x2="967" y2="1230" stroke="var(--chart-blue)" stroke-width="2.5"/>
  <text x="969" y="1234" font-size="11">Cumulative Percent Complete</text>
  <line x1="1150" y1="1230" x2="1175" y2="1230" stroke="var(--chart-orange)" stroke-width="2.5"/>
  <text x="1177" y="1234" font-size="11">Cumulative Cost</text>
</svg>

</div>
</body>
</html>
```